Design Postcards for our Dog Walking Company

Hi designer! Please create an improved design for our postcards :)

Attached are some samples of our past designs. We're looking for better ones but you can check them out so you can see what we've done in the past. They have all of our brand colors. I also attached two versions of our logo.

We are a dog walking and pet sitting company based in Southeastern CT.
Our services are Dog Walking, Pet Sitting, Adventure Hikes, Cat Care, Overnights.
The contact information to go on the postcard is 860-555-0187 CTBriskTails.com info@ctbrisktails
** - Create 3 designs for the 3 sizes (small, medium, and large)**
- Follow Measurement Guidelines as per the documents attached.
- Follow best practices as per the "Blueprint for a Winning Mailer" (the offer is a Free Meet & Greet)
- Please leave space for a QR code and give me the measurements of said QR code (I will generate it at a later date)
- Please check our Zoobly reviews for any testimonial to be included
- I've attached many pictures for you to use for the graphic
- Make sure the file has a bleed
- Brand Guidelines: All of our fonts are the Fredoka Family (attached)
- Colors (present in the samples provided)

PLEASE ONLY CONTACT ME THROUGH ARTSQUIRE!
**PLEASE** DO NOT CONTACT US ON FRIENDLOOP, NOT ON SNAPVERSE, DO NOT EMAIL, DO NOT CALL US.

Thank you for your help! :)
Marisol

Target Market(s)

Pet Owners in the neighborhoods we serve who are not yet clients

Industry/Entity Type

Dog Walking

Other font styles liked:
• I've attached the font file Fredoka family

Colors
0094D4
00A9DD
6FCCEA
C7EBF8
E9F6FB
E54698
E96AAD
F1A4CE
F9D9EA
FCEFF6

Requirements
Must have
• ** - Create 3 designs for the 3 sizes (small, medium, and large)** - Follow Measurement Guidelines as per the documents attached. - Follow best practices as per the "Blueprint for a Winning Mailer" (the offer is a Free Meet & Greet) - Please leave space for a QR code and give me the measurements of said QR code (I will generate it at a later date) - Please check our Zoobly reviews for any testimonial to be included
Nice to have
• Up to you
Should not have
• Any fonts or colors that are not our branding

```html
<!DOCTYPE html>
<html lang="en">
<head>
<meta charset="utf-8">
<title>Harborline Brisk Tails Postcard</title>
<link href="https://fonts.googleapis.com/css2?family=Fredoka:wght@400;500;600;700&family=Saira+Condensed:wght@500;700;800&family=Barlow+Condensed:wght@400;500;700&display=swap" rel="stylesheet">
<style>
  :root{
    --stage:#a6f4f8;
    --panel:#eff8fc;
    --blue-deep:#0094d4;
    --blue:#00a9dd;
    --blue-soft:#6fccea;
    --blue-pale:#e4f3fb;
    --pink-deep:#e54698;
    --pink:#e96aad;
    --pink-soft:#f1a4ce;
    --ink:#111111;
    --white:#ffffff;
    --sea:#4d6f96;
    --sand:#d3c4b2;
  }
  *{box-sizing:border-box;margin:0;padding:0}
  html,body{width:864px;height:1200px;overflow:hidden}
  body{background:var(--stage);position:relative;font-family:"Fredoka",sans-serif;color:var(--ink)}

  .postcard{position:absolute;left:93px;width:678px;height:452px;background:var(--panel);overflow:hidden}
  .postcard--front{top:102px}
  .postcard--back{top:647px}

  /* front */
  .front-info{position:absolute;left:0;top:0;width:308px;height:452px}
  .headline{position:absolute;left:24px;top:20px;width:270px;white-space:nowrap;color:var(--blue);font-weight:700;font-size:37px;line-height:44px;letter-spacing:1px}
  .services{position:absolute;left:24px;top:128px;list-style:none;font-weight:500;font-size:20px;line-height:26px;letter-spacing:1px}
  .availability{position:absolute;left:203px;top:133px;width:82px;text-align:center;color:var(--pink)}
  .availability svg{display:block;width:80px;height:78px}
  .availability .label{font-size:13px;letter-spacing:1px;margin-top:4px;line-height:14px}
  .availability .hours{font-size:17px;font-weight:600;line-height:18px}
  .credentials{position:absolute;left:24px;top:279px;color:var(--blue);font-weight:500;font-size:15.5px;letter-spacing:.6px;white-space:nowrap}
  .brand-mark{position:absolute;display:flex;flex-direction:column;align-items:center;justify-content:center;text-align:center;gap:6px;color:var(--blue-soft);font-weight:700;letter-spacing:1px;line-height:1.05}
  .brand-mark .dot{width:30px;height:30px;border-radius:50%;background:var(--pink-soft)}
  .brand-mark--front{left:20px;top:322px;width:106px;height:104px;font-size:14px}
  .front-contact{position:absolute;left:130px;top:347px;width:170px;text-align:center;font-size:13.5px;line-height:18.5px}
  .front-contact .phone{font-size:15.5px}
  .hero-photo{position:absolute;left:308px;top:0;width:370px;height:452px;
    background:linear-gradient(180deg,var(--sea) 0%,#7f95ad 30%,var(--sand) 55%,#e6e2dc 100%)}

  /* back */
  .why-box{position:absolute;left:22px;top:23px;width:226px;height:229px;background:var(--pink-soft);border:1px solid var(--pink);border-radius:10px;box-shadow:0 1px 4px rgba(0,0,0,.25);padding:9px 0 0 9px}
  .why-title{font-family:"Saira Condensed",sans-serif;font-weight:800;font-size:25px;letter-spacing:1.8px;line-height:26px;padding-left:1px}
  .why-list{list-style:none;margin-top:10px;font-family:"Saira Condensed",sans-serif;font-weight:800;font-size:13.2px;letter-spacing:1.2px;line-height:20.1px}
  .why-list li{display:flex;align-items:center;gap:7px}
  .why-list li::before{content:"";width:8px;height:8px;border-radius:50%;background:var(--white);flex:none}
  .offer-box{position:absolute;left:22px;top:270px;width:226px;height:60px;background:var(--blue-pale);border-radius:9px;box-shadow:0 1px 4px rgba(0,0,0,.25);text-align:center;color:var(--blue);font-family:"Barlow Condensed",sans-serif;font-weight:500;font-size:22px;line-height:26px;padding-top:5px}
  .brand-mark--back{left:18px;top:340px;width:94px;height:96px;font-size:12.5px}
  .back-contact{position:absolute;left:118px;top:354px;width:136px;text-align:center;font-size:11.5px;line-height:16px}
  .back-contact .cta{font-family:"Saira Condensed",sans-serif;font-weight:800;color:var(--blue);font-size:20px;letter-spacing:1.5px;line-height:22px}
  .back-contact .phone{font-size:16px;line-height:20px}
  .testimonial{position:absolute;left:268px;top:23px;width:265px;height:130px;border:1px solid var(--blue-soft);border-radius:10px;padding:8px 10px;font-family:"Barlow Condensed",sans-serif;font-size:13.6px;line-height:15.6px;text-align:justify}
  .testimonial .mark{color:var(--blue);font-weight:700;font-size:15px}
  .testimonial cite{font-style:normal;font-weight:700;letter-spacing:.5px}
  .qr-space{position:absolute;left:543px;top:37px;width:102px;height:102px;border:1px solid var(--blue-deep);background:var(--white);display:flex;flex-direction:column;align-items:center;justify-content:center;font-family:"Saira Condensed",sans-serif;font-weight:800;letter-spacing:1.2px}
  .qr-space .qr-title{font-size:19px;line-height:22px}
  .qr-space .qr-size{font-size:13px;margin-top:6px}
  .mailing-area{position:absolute;left:268px;top:184px;width:410px;height:268px;background:var(--white)}
</style>
</head>
<body>

<section class="postcard postcard--front">
  <div class="front-info">
    <h1 class="headline">HAPPY PET<br>GUARANTEED</h1>
    <ul class="services">
      <li>DOG WALKING</li>
      <li>DOG HIKING</li>
      <li>PET SITTING</li>
      <li>CAT CARE</li>
      <li>OVERNIGHTS</li>
    </ul>
    <div class="availability">
      <svg viewBox="0 0 80 78" fill="none" stroke="currentColor" stroke-width="4" stroke-linecap="round">
        <rect x="3" y="9" width="50" height="46" rx="4"/>
        <line x1="3" y1="20" x2="53" y2="20"/>
        <line x1="13" y1="3" x2="13" y2="12"/><line x1="23" y1="3" x2="23" y2="12"/><line x1="33" y1="3" x2="33" y2="12"/><line x1="43" y1="3" x2="43" y2="12"/>
        <g fill="currentColor" stroke="none">
          <rect x="9" y="25" width="7" height="6"/><rect x="19" y="25" width="7" height="6"/><rect x="29" y="25" width="7" height="6"/><rect x="39" y="25" width="7" height="6"/>
          <rect x="9" y="34" width="7" height="6"/><rect x="19" y="34" width="7" height="6"/><rect x="29" y="34" width="7" height="6"/>
          <rect x="9" y="43" width="7" height="6"/><rect x="19" y="43" width="7" height="6"/>
        </g>
        <circle cx="56" cy="54" r="20" fill="var(--panel)"/>
        <polyline points="56,42 56,54 63,60"/>
      </svg>
      <div class="label">AVAILABLE</div>
      <div class="hours">24/7/365</div>
    </div>
    <p class="credentials">INSURED + BONDED &amp; PET CPR</p>
    <div class="brand-mark brand-mark--front"><span class="dot"></span><span>HARBORLINE<br>BRISK TAILS</span></div>
    <address class="front-contact" style="font-style:normal">
      <div class="phone">860-555-0187</div>
      <div>info@ctbrisktails.com</div>
      <div>www.CTBriskTails.com</div>
    </address>
  </div>
  <div class="hero-photo" role="img" aria-label="Photo of a fluffy white dog smiling on a sandy beach beside the sea"></div>
</section>

<section class="postcard postcard--back">
  <div class="why-box">
    <h2 class="why-title">WHY CHOOSE US?</h2>
    <ul class="why-list">
      <li>RELIABLE TEAM OF SITTERS</li>
      <li>INSURED &amp; BONDED</li>
      <li>PET FIRST AID &amp; CPR CERTIFIED</li>
      <li>BACKGROUND CHECKED</li>
      <li>REPORTS AFTER EVERY SERVICE</li>
      <li>AVAILABLE 24/7/365</li>
      <li>BOOK &amp; PAY ONLINE</li>
      <li>STAFF CONTINUED TRAINING</li>
      <li>LOCALLY OWNED &amp; OPERATED</li>
    </ul>
  </div>
  <div class="offer-box">BOOK YOUR<br>FREE MEET &amp; GREET</div>
  <div class="brand-mark brand-mark--back"><span class="dot"></span><span>HARBORLINE<br>BRISK TAILS</span></div>
  <address class="back-contact" style="font-style:normal">
    <div class="cta">CALL TODAY</div>
    <div class="phone">860-555-0187</div>
    <div>info@ctbrisktails.com</div>
    <div>www.CTBriskTails.com</div>
  </address>
  <blockquote class="testimonial">
    <span class="mark">&ldquo;</span> Harborline Brisk Tails has been a dream come true! They are reliable, loving to our pets, and a business we rely on all the time! I don't know what we would have done without Harborline Brisk Tails! They have been taking care of our 2 cats, whenever we are out of town, since they were kittens! A true CT Shoreline Gem!!! - <cite>Renata Colby</cite><span class="mark">&rdquo;</span>
  </blockquote>
  <div class="qr-space">
    <div class="qr-title">QR CODE</div>
    <div class="qr-size">0.9 X 0.9 in</div>
  </div>
  <div class="mailing-area"></div>
</section>

</body>
</html>
```